Need a website for our company

We need a website for our company to showcase all our work for customers to see.
We do all phases of home improvement:
Dormers/Extensions
Basement Remodel
Masonry/Concrete/Pavers/Asphalt
Cultured Stone Veneer
Kitchens
Bathrooms
Pool designs
Outdoor Bathroom
Outdoor Kitchens
Tile work
For reference, something similar to this website: https://brightoakrenovations.example/
Target Market(s)
We are trying to target homeowners.
Coding
Number of Pages Required
Look and feel

```html
<!DOCTYPE html>
<html lang="en">
<head>
<meta charset="utf-8">
<title>Harlow &amp; Sons Construction Inc</title>
<link href="https://fonts.googleapis.com/css2?family=Roboto:wght@400;500;700&display=swap" rel="stylesheet">
<style>
:root{
  --ink:#2b2b2b;
  --dark:#333333;
  --body:#555555;
  --muted:#8a8a8a;
  --white:#ffffff;
  --hero-a:#d9d2ca;
  --hero-b:#a8c4cf;
}
*{margin:0;padding:0;box-sizing:border-box}
html,body{width:1200px;height:3645px;overflow:hidden}
body{position:relative;background:var(--white);font-family:"Roboto",Arial,sans-serif;color:var(--ink)}
.abs{position:absolute}

/* top bar */
.topline{left:0;top:0;width:1200px;height:4px;background:var(--dark)}
.contact-strip{left:630px;top:0;width:570px;height:42px;background:var(--dark);clip-path:polygon(0 0,100% 0,100% 100%,12px 100%)}
.contact-strip .item{position:absolute;top:13px;color:var(--white);font-size:14px;font-weight:500;display:flex;align-items:center;gap:12px;white-space:nowrap}
.contact-strip svg{width:18px;height:18px}

/* header brand: plain name */
.brand{left:110px;top:66px;display:flex;align-items:center;gap:8px;font-size:13px;font-weight:700;color:var(--dark);white-space:nowrap}
.brand .mark{width:12px;height:12px;background:var(--dark)}
.nav{top:74px;font-size:16px;color:var(--body);white-space:nowrap}
.btn{display:flex;align-items:center;justify-content:center;background:var(--dark);color:var(--white);font-weight:500;font-size:16px;white-space:nowrap;clip-path:polygon(9px 0,100% 0,calc(100% - 9px) 100%,0 100%)}
.quote{left:927px;top:64px;width:160px;height:42px}

/* hero */
.hero{left:0;top:126px;width:1200px;height:573px;background:linear-gradient(90deg,var(--hero-a) 0%,#e4ddd3 35%,var(--hero-b) 70%,#5a9fb5 100%)}
.hero-title{left:110px;top:268px;font-weight:700;color:var(--ink);line-height:1;white-space:nowrap}
.hero-title .l1{font-size:50px}
.hero-title .l2{font-size:62px;margin-top:4px}
.hero-text{left:110px;top:402px;width:340px;font-size:16px;line-height:27px;color:var(--ink)}
.start{left:110px;top:505px;width:166px;height:43px}

/* services */
.section-title{left:0;width:1200px;text-align:center;font-size:42px;font-weight:700;color:var(--ink)}
.section-sub{left:262px;width:676px;text-align:center;font-size:16px;line-height:26px;color:var(--body)}
.svc-photo{width:488px;height:385px;border-radius:24px;border:2px solid var(--dark);overflow:hidden}
.svc-title{font-size:30px;font-weight:700;color:var(--ink);white-space:nowrap}
.svc-text{width:400px;font-size:13.5px;line-height:25.7px;color:var(--body)}
.more{width:164px;height:42px}
.load{left:519px;top:2707px;width:163px;height:41px}

/* about */
.about{left:0;top:2823px;width:1200px;height:509px;background:var(--dark)}
.about-title{left:132px;top:2928px;font-size:30px;font-weight:700;color:var(--white)}
.about-text{left:132px;top:2974px;width:400px;font-size:13.5px;line-height:25.7px;color:#dddddd}
.about-more{left:133px;top:3177px;width:164px;height:42px;background:var(--white);color:var(--dark)}
.about-photo{left:597px;top:2905px;width:566px;height:344px;background:linear-gradient(135deg,#6d8a5a 0%,#9a948a 45%,#4d4d4d 100%)}

/* footer */
.foot-brand{left:110px;top:3515px;width:364px;display:flex;align-items:center;justify-content:center;gap:10px;font-size:18px;font-weight:500;color:var(--body);white-space:nowrap}
.foot-brand .mark{width:16px;height:16px;background:var(--body)}
.ico{width:60px;height:60px;border-radius:50%;background:var(--dark);display:flex;align-items:center;justify-content:center}
.ico svg{width:24px;height:24px}
.info{font-size:15px;line-height:23px;color:var(--body)}
.info b{font-weight:500;color:var(--ink)}
.copyright{left:0;top:3606px;width:1200px;text-align:center;font-size:12px;color:var(--body)}
</style>
</head>
<body>

<div class="abs topline"></div>
<div class="abs contact-strip">
  <div class="item" style="left:36px">
    <svg viewBox="0 0 24 24" fill="none" stroke="#fff" stroke-width="2"><path d="M5 3h4l2 5-3 2a11 11 0 0 0 6 6l2-3 5 2v4a2 2 0 0 1-2 2A17 17 0 0 1 3 5a2 2 0 0 1 2-2z"/></svg>
    +1 555 0142-300
  </div>
  <div class="item" style="left:224px">
    <svg viewBox="0 0 24 24" fill="none" stroke="#fff" stroke-width="2"><rect x="3" y="5" width="18" height="14"/><path d="M3 5l9 7 9-7"/></svg>
    info@harlowsonsbuild.example
  </div>
</div>

<div class="abs brand"><span class="mark"></span>Harlow &amp; Sons Construction Inc</div>
<div class="abs nav" style="left:439px">Home</div>
<div class="abs nav" style="left:542px">About Us</div>
<div class="abs nav" style="left:666px">Our Services</div>
<div class="abs nav" style="left:818px">Contact Us</div>
<div class="abs btn quote">Get A Quote</div>

<div class="abs hero" role="img" aria-label="Luxury home with terracotta roof beside a curved swimming pool"></div>
<div class="abs hero-title"><div class="l1">WELCOME TO</div><div class="l2">HARLOW &amp; SONS.</div></div>
<p class="abs hero-text">It is a long established fact that a reader will be distracted by the readable content of a page when looking at its layout.</p>
<div class="abs btn start">Get Started</div>

<h2 class="abs section-title" style="top:762px">OUR SERVICES</h2>
<p class="abs section-sub" style="top:824px">It is a long established fact that a reader will be distracted by the readable content of a page when looking at its layout.</p>

<!-- Dormers -->
<h3 class="abs svc-title" style="left:132px;top:962px">DORMERS/EXTENSIONS</h3>
<p class="abs svc-text" style="left:132px;top:1007px">It is a long established fact that a reader will be distracted by the readable content of a page when looking at its layout. The point of using Lorem Ipsum is that it has a more-or-less normal distribution of letters, as opposed to using 'Content here, content here', making it look like readable English. Many desktop publishing packages and web page editors now use Lorem Ipsum as their default model text, and a search</p>
<div class="abs btn more" style="left:133px;top:1211px">Read More</div>
<div class="abs svc-photo" style="left:579px;top:917px;background:linear-gradient(180deg,#8fb4e0 0%,#d9c29a 55%,#4f6e3a 100%)" role="img" aria-label="Timber house frame under construction"></div>

<!-- Basement -->
<div class="abs svc-photo" style="left:133px;top:1368px;background:linear-gradient(135deg,#d8cdb8 0%,#a07850 55%,#3a2a20 100%)" role="img" aria-label="Finished basement with bar stools and leather seating"></div>
<h3 class="abs svc-title" style="left:667px;top:1413px">BASEMENT REMODEL</h3>
<p class="abs svc-text" style="left:667px;top:1458px">It is a long established fact that a reader will be distracted by the readable content of a page when looking at its layout. The point of using Lorem Ipsum is that it has a more-or-less normal distribution of letters, as opposed to using 'Content here, content here', making it look like readable English. Many desktop publishing packages and web page editors now use Lorem Ipsum as their default model text, and a search</p>
<div class="abs btn more" style="left:668px;top:1662px">Read More</div>

<!-- Kitchens -->
<h3 class="abs svc-title" style="left:132px;top:1864px">KITCHENS</h3>
<p class="abs svc-text" style="left:132px;top:1909px">It is a long established fact that a reader will be distracted by the readable content of a page when looking at its layout. The point of using Lorem Ipsum is that it has a more-or-less normal distribution of letters, as opposed to using 'Content here, content here', making it look like readable English. Many desktop publishing packages and web page editors now use Lorem Ipsum as their default model text, and a search</p>
<div class="abs btn more" style="left:133px;top:2113px">Read More</div>
<div class="abs svc-photo" style="left:579px;top:1820px;background:linear-gradient(180deg,#f0ece4 0%,#6b6b6b 50%,#e8e8e8 100%)" role="img" aria-label="Modern kitchen with grey cabinets and white island"></div>

<!-- Pool -->
<div class="abs svc-photo" style="left:133px;top:2271px;background:linear-gradient(90deg,#3d9ad0 0%,#7cc4e6 50%,#bfb6a6 60%,#d4ccbd 100%)" role="img" aria-label="Pool edge with flagstone paving"></div>
<h3 class="abs svc-title" style="left:667px;top:2316px">POOL DESIGNS</h3>
<p class="abs svc-text" style="left:667px;top:2361px">It is a long established fact that a reader will be distracted by the readable content of a page when looking at its layout. The point of using Lorem Ipsum is that it has a more-or-less normal distribution of letters, as opposed to using 'Content here, content here', making it look like readable English. Many desktop publishing packages and web page editors now use Lorem Ipsum as their default model text, and a search</p>
<div class="abs btn more" style="left:668px;top:2565px">Read More</div>

<div class="abs btn load">Load More</div>

<!-- About -->
<div class="abs about"></div>
<h2 class="abs about-title">ABOUT US</h2>
<p class="abs about-text">It is a long established fact that a reader will be distracted by the readable content of a page when looking at its layout. The point of using Lorem Ipsum is that it has a more-or-less normal distribution of letters, as opposed to using 'Content here, content here', making it look like readable English. Many desktop publishing packages and web page editors now use Lorem Ipsum as their default model text, and a search</p>
<div class="abs btn about-more">Read More</div>
<div class="abs about-photo" role="img" aria-label="Outdoor patio with lawn and seating"></div>

<!-- Footer -->
<div class="abs foot-brand"><span class="mark"></span>Harlow &amp; Sons Construction Inc</div>

<div class="abs ico" style="left:542px;top:3413px">
  <svg viewBox="0 0 24 24" fill="none" stroke="#fff" stroke-width="2"><path d="M12 22s7-7 7-12a7 7 0 0 0-14 0c0 5 7 12 7 12z"/><circle cx="12" cy="10" r="2.5"/></svg>
</div>
<p class="abs info" style="left:616px;top:3422px;width:240px">17Y, It is a long established fact that a reader will be</p>

<div class="abs ico" style="left:894px;top:3413px">
  <svg viewBox="0 0 24 24" fill="none" stroke="#fff" stroke-width="2"><path d="M5 3h4l2 5-3 2a11 11 0 0 0 6 6l2-3 5 2v4a2 2 0 0 1-2 2A17 17 0 0 1 3 5a2 2 0 0 1 2-2z"/></svg>
</div>
<p class="abs info" style="left:969px;top:3422px"><b>Contact:</b><br>+1 555 0142-300</p>

<div class="abs ico" style="left:542px;top:3500px">
  <svg viewBox="0 0 24 24" fill="none" stroke="#fff" stroke-width="2"><rect x="3" y="5" width="18" height="14"/><path d="M3 5l9 7 9-7"/></svg>
</div>
<p class="abs info" style="left:616px;top:3507px"><b>Email Address:</b><br>info@harlowsons.example</p>

<div class="abs ico" style="left:894px;top:3500px">
  <svg viewBox="0 0 24 24" fill="none" stroke="#fff" stroke-width="2"><circle cx="12" cy="12" r="9"/><path d="M3 12h18M12 3c3 3 3 15 0 18M12 3c-3 3-3 15 0 18"/></svg>
</div>
<p class="abs info" style="left:969px;top:3507px"><b>Website:</b><br>www.harlowsons.example</p>

<p class="abs copyright">© Copyright 2023 Harlow &amp; Sons Constructions Inc | All Rights Reserved.</p>

</body>
</html>
```